Flyer for rhytmic gymnastics school

Hello everybody. We are planning to launch advertising campaign for our rhytmic gymnastics school. The flyers will be distributed directly to people throughout the city putting them on doorknobs. So the design should be very attractive and clear. Our goal is to attract small girls age 3-5. The idea and concept of the flyer is up to you but we just want to empasize the attractivness and benefits of this sport - basically it's a combination of ballet, gymnastics and dance. We even consider using cartoonish style of the flyer. We also have our logo, it's attached. The school is located in Southern California, with a diverse population. Chinese and Korean families that recently came to the US probably will be the main target audience since they know about this sport more. So one the goals is to show people who have never heard about Rhytmic Gymnastics what this sport is about. We need to design both sides of the flyers. We think that on one side of the flyer should be placed photo of our school (it should be ready in two days) and information about facility, adress etc. And as I mentioned one side should be creative and unusual to attract kids and parents. Here is some information about PA in general

Looking for new sport for your daughter?
Try Rhythmic Gymnastics! It’s an Olympic Sport!

• Enrollment is now open for Girls 3, 5-5 year old
• Competitive opportunity or recreational classes
• Instruction based on Russian School of Rhythmic Gymnastics
• A team of professional coaches
Brand new facility exlusively for rhytmic gymnastics activity
FREE introductory class!

Rhythmic Gymnastics is a discipline combining grace, coordination, agility and
artistry.
Rhythmic gymnastics combines ballet and creative movements to music, while
working with ribbons, balls, hoops, ropes and clubs in a choreographed danceand-tumble routine. Rhythmic gymnastics creates beautiful strong bodies as well
as improving child’s cognitive abilities

Target Market(s)

Families with small kids

Industry/Entity Type

Advertising

Requirements
Must have
• We see the flyer as a double sided flat A6 size, but again it's up to you.
Location
41876 Vista Moreno ct
Laguna Hills, CA
92653
www.pelmora-academy.us
Phone # 714 382 5046
e-mail kids@pelmora-academy.us
Facebook page https://www.facebook.com/TavelleRhythmicGymnastics

```html
<!DOCTYPE html>
<html lang="en">
<head>
<meta charset="utf-8">
<title>Pelmora Academy of Rhythmic Gymnastics – Flyer</title>
<link rel="stylesheet" href="https://fonts.googleapis.com/css2?family=Luckiest+Guy&family=Open+Sans:wght@400;600;700;800&display=swap">
<style>
  :root {
    --yellow: #fff200;
    --sky: #29a9e0;
    --purple: #8e3f9b;
    --pink: #e5157a;
    --magenta: #c4137f;
    --red: #e8202a;
    --ink: #2b2b2b;
    --slate: #4a4a6a;
    --bg: #ffffff;
  }
  * { box-sizing: border-box; margin: 0; padding: 0; }
  html, body { width: 1200px; height: 1049px; overflow: hidden; background: var(--bg); }
  body { position: relative; font-family: "Open Sans", Arial, sans-serif; color: var(--ink); }

  .flyer {
    position: absolute;
    width: 498px; height: 774px;
    overflow: hidden;
    background: linear-gradient(180deg, #ffffff 0%, #f3f9ff 55%, #fbe8f2 100%);
    box-shadow: 0 0 0 1px #e6e6e6;
  }
  .flyer--front { left: 48px; top: 18px; }
  .flyer--back  { left: 640px; top: 150px; }

  .display {
    font-family: "Luckiest Guy", "Arial Black", Impact, sans-serif;
    font-weight: 400; text-transform: uppercase; letter-spacing: 0.5px;
  }

  /* ---------- front ---------- */
  .front-top {
    position: absolute; left: 0; top: 0; width: 100%; height: 200px;
    background: linear-gradient(180deg, var(--yellow) 0%, #fff86a 70%, rgba(255,255,255,0) 100%);
  }
  .front-headline {
    position: absolute; left: 0; top: 42px; width: 100%;
    text-align: center; font-size: 29px; line-height: 36px; color: var(--purple);
  }
  .front-headline .accent { color: var(--sky); }

  .photo-gymnast {
    position: absolute; left: 282px; top: 112px; width: 200px; height: 280px;
    border-radius: 50% 40% 30% 45%;
    background: radial-gradient(circle at 45% 45%, #f6c6b5 0%, #e2439a 35%, #8a62c9 60%, rgba(255,255,255,0) 78%);
  }
  .try-block { position: absolute; left: 16px; top: 170px; width: 266px; text-align: center; }
  .try-block .try { font-size: 42px; line-height: 46px; color: var(--pink); }
  .try-block .sport { font-size: 33px; line-height: 40px; color: var(--sky); }
  .try-block .olympic { font-size: 18px; line-height: 30px; color: var(--pink); }

  .enroll-band {
    position: absolute; left: 0; top: 392px; width: 100%; height: 104px;
    background: linear-gradient(90deg, var(--sky) 0%, #4ec0ec 100%);
    color: #fff; text-align: center; padding-top: 16px; padding-right: 70px;
    font-size: 27px; line-height: 34px; font-weight: 700;
  }
  .free-arrow { position: absolute; left: 300px; top: 468px; width: 200px; height: 130px; }

  .join-today {
    position: absolute; left: 34px; top: 516px; font-size: 46px; line-height: 52px;
    color: var(--red); transform: rotate(-8deg);
  }
  .contact { position: absolute; left: 48px; font-size: 20px; font-weight: 700; display: flex; align-items: center; gap: 10px; }
  .contact svg { width: 22px; height: 18px; }
  .contact--phone { top: 640px; color: var(--sky); }
  .contact--mail  { top: 668px; color: var(--magenta); }
  .address { position: absolute; left: 48px; top: 714px; font-size: 18px; color: var(--ink); white-space: nowrap; }

  .brand { position: absolute; display: flex; align-items: center; gap: 8px; }
  .brand .dot { width: 14px; height: 14px; border-radius: 50%; background: var(--pink); flex: none; }
  .brand .name { font-size: 13px; line-height: 16px; font-weight: 600; color: var(--magenta); }
  .brand--front { left: 290px; top: 612px; width: 190px; }
  .site { position: absolute; left: 298px; top: 584px; font-size: 14px; font-weight: 700; color: var(--magenta); white-space: nowrap; }

  /* ---------- back ---------- */
  .back-top {
    position: absolute; left: 0; top: 0; width: 100%; height: 120px;
    background: var(--yellow);
  }
  .back-curve { position: absolute; left: 0; top: 80px; width: 498px; height: 80px; }
  .back-title {
    position: absolute; left: 50px; top: 22px; width: 430px; text-align: center;
    font-size: 18px; line-height: 23px; color: var(--purple);
  }
  .back-title .accent { color: var(--sky); }
  .about {
    position: absolute; left: 42px; top: 160px; width: 222px;
    font-size: 11.5px; line-height: 15px; text-align: right; color: var(--ink);
  }
  .photo-gymnast--small {
    position: absolute; left: 290px; top: 150px; width: 170px; height: 175px;
    border-radius: 50%;
    background: radial-gradient(circle at 50% 50%, #f6c6b5 0%, #e2439a 35%, #8a62c9 58%, rgba(255,255,255,0) 75%);
  }
  .offers { position: absolute; right: 34px; top: 334px; width: 300px; text-align: right; }
  .offers h3 { font-size: 13px; font-weight: 600; color: var(--magenta); margin-bottom: 4px; }
  .offers li { list-style: none; font-size: 12.5px; line-height: 16px; color: var(--slate); margin-bottom: 2px; }
  .offers li::before { content: "✔ "; color: var(--pink); }

  .burst { position: absolute; left: 30px; top: 440px; width: 190px; height: 190px; }
  .burst-text {
    position: absolute; left: 58px; top: 490px; width: 134px; text-align: center;
    font-size: 15px; line-height: 18px; font-weight: 800; color: #fff;
  }
  .school-link { position: absolute; left: 0; top: 0; width: 498px; height: 774px; pointer-events: none; }
  .photo-school {
    position: absolute; left: 244px; top: 452px; width: 220px; height: 220px; border-radius: 50%;
    border: 9px solid var(--magenta);
    background: linear-gradient(180deg, #ffffff 0%, #eef7ff 100%);
    display: flex; align-items: center; justify-content: center; text-align: center;
    font-size: 34px; line-height: 38px; font-weight: 600; color: var(--sky);
  }
  .brand--back { left: 38px; top: 644px; width: 190px; }
  .address--back { left: 38px; top: 690px; font-size: 17px; }
  .back-contacts { position: absolute; left: 38px; top: 726px; display: flex; gap: 26px; font-size: 18px; font-weight: 700; white-space: nowrap; }
  .back-contacts span { display: flex; align-items: center; gap: 8px; }
  .back-contacts svg { width: 20px; height: 16px; }
  .back-contacts .phone { color: var(--sky); }
  .back-contacts .mail { color: var(--magenta); }
</style>
</head>
<body>

<svg width="0" height="0" style="position:absolute">
  <defs>
    <symbol id="icon-phone" viewBox="0 0 22 18"><path d="M2 6c0-3 4-4 9-4s9 1 9 4l-3 2-2-2h-8l-2 2zM5 9h12l2 7H3z" fill="currentColor"/><circle cx="11" cy="12" r="2" fill="#fff"/></symbol>
    <symbol id="icon-mail" viewBox="0 0 22 18"><rect x="3" y="3" width="17" height="12" fill="none" stroke="currentColor" stroke-width="2"/><path d="M3 3l8.5 7L20 3" fill="none" stroke="currentColor" stroke-width="2"/><path d="M0 7h3M0 11h3" stroke="currentColor" stroke-width="1.5"/></symbol>
  </defs>
</svg>

<!-- Front side -->
<section class="flyer flyer--front">
  <div class="front-top"></div>
  <h1 class="front-headline display">Looking for <span class="accent">new sport</span><br>for your daughter?</h1>
  <div class="photo-gymnast" role="img" aria-label="Photo of a young gymnast in a pink leotard holding a gold ball in a backbend pose"></div>
  <div class="try-block display">
    <div class="try">Try</div>
    <div class="sport">Rhythmic<br>Gymnastics!</div>
    <div class="olympic">It's an Olympic Sport!</div>
  </div>
  <div class="enroll-band">Enrollment is now open<br>for Girls 3-5 year old</div>
  <svg class="free-arrow" viewBox="0 0 200 130">
    <polygon points="10,30 150,20 150,0 198,55 150,110 150,90 10,96" fill="var(--yellow)"/>
    <text x="28" y="72" font-family="Luckiest Guy, Arial Black, Impact, sans-serif" font-size="40" fill="#111" transform="rotate(-8 80 60)">FREE</text>
    <text x="14" y="104" font-family="Open Sans, Arial, sans-serif" font-weight="800" font-size="13" fill="#111" transform="rotate(-8 80 90)">INTRODUCTORY CLASS</text>
  </svg>
  <div class="join-today display">Join<br>Today!</div>
  <div class="site">www.pelmora-academy.us</div>
  <div class="brand brand--front"><span class="dot"></span><span class="name">Pelmora Academy of Rhythmic Gymnastics</span></div>
  <div class="contact contact--phone"><svg><use href="#icon-phone"/></svg>714 382 5046</div>
  <div class="contact contact--mail"><svg><use href="#icon-mail"/></svg>kids@pelmora-academy.us</div>
  <div class="address">41876 Vista Moreno ct, Laguna Hills, CA 92653</div>
</section>

<!-- Back side -->
<section class="flyer flyer--back">
  <div class="back-top"></div>
  <svg class="back-curve" viewBox="0 0 498 80" preserveAspectRatio="none">
    <path d="M0 30 Q250 80 498 40 L498 50 Q250 95 0 45 Z" fill="var(--sky)"/>
    <path d="M0 0 H498 V40 Q250 80 0 30 Z" fill="var(--yellow)"/>
  </svg>
  <h2 class="back-title display"><span class="accent">Rhythmic Gymnastics</span> is a discipline combining grace, coordination, agility and artistry.</h2>
  <p class="about">Rhythmic gymnastics combines ballet and creative movements to music, while working with ribbons, balls, hoops, ropes and clubs in a choreographed dance and tumble routine. Rhythmic gymnastics creates beautiful strong bodies as well as improving child's cognitive abilities</p>
  <div class="photo-gymnast--small" role="img" aria-label="Photo of a young gymnast with a gold ball"></div>
  <div class="offers">
    <h3>Pelmora Academy Offers</h3>
    <ul>
      <li>Competitive opportunity or recreational classes</li>
      <li>Instruction based on Russian School of Rhythmic Gymnastics</li>
      <li>A team of professional coaches</li>
    </ul>
  </div>
  <svg class="school-link" viewBox="0 0 498 774">
    <line x1="440" y1="500" x2="498" y2="470" stroke="var(--magenta)" stroke-width="9"/>
  </svg>
  <svg class="burst" viewBox="0 0 180 180">
    <polygon fill="var(--pink)" points="178,90 161.5,109.2 166.2,134 142.3,142.3 134,166.2 109.2,161.5 90,178 70.8,161.5 46,166.2 37.7,142.3 13.8,134 18.5,109.2 2,90 18.5,70.8 13.8,46 37.7,37.7 46,13.8 70.8,18.5 90,2 109.2,18.5 134,13.8 142.3,37.7 166.2,46 161.5,70.8"/>
    <circle cx="90" cy="90" r="68" fill="none" stroke="#fff" stroke-width="1.5" stroke-dasharray="4 3"/>
  </svg>
  <div class="burst-text">Brand new facility exclusively for rhytmic gymnastics activity</div>
  <div class="photo-school">Photo<br>of<br>school</div>
  <div class="brand brand--back"><span class="dot"></span><span class="name">Pelmora Academy of Rhythmic Gymnastics</span></div>
  <div class="address address--back">41876 Vista Moreno ct, Laguna Hills, CA 92653</div>
  <div class="back-contacts">
    <span class="phone"><svg><use href="#icon-phone"/></svg>714 382 5046</span>
    <span class="mail"><svg><use href="#icon-mail"/></svg>kids@pelmora-academy.us</span>
  </div>
</section>

</body>
</html>
```